Nutracuetical Company website. Selling 1 supplement product

I need a WordPress eCommerce site made for 1 product. We sell a probiotic with advanced technology. I want the site to be very informative with a health and wellness feel. Bright pictures with people smiling, etc... I need a separate page highlighting the lab test results

Currently on Parcelora https://www.parcelora.com/gp/product/Q73KD2XR4M

Target Market(s)

People with intestinal issues. IBS Chrons Irregularity

Industry/Entity Type

Health And Wellness

Number of Pages Required

4 page

Requirements
Must have
• I want the site to be very informative with a health and wellness feel. Bright pictures with people smiling, etc... I need a separate page highlighting the lab test results
Nice to have
• Colors should match the logo

```html
<!DOCTYPE html>
<html lang="en">
<head>
<meta charset="utf-8">
<title>Verdant Biome — Probiotic Supplements</title>
<link rel="stylesheet" href="https://fonts.googleapis.com/css2?family=Roboto:wght@400;500;700&family=Open+Sans:wght@400;600;700&display=swap">
<style>
:root{
  --green:#7cb82f;
  --green-dark:#5a9216;
  --green-pale:#eef4e2;
  --blue:#2e7fd6;
  --sky:#2fa4e7;
  --ink:#1d1d1d;
  --text:#555;
  --muted:#777;
  --grey-bg:#f6f6f6;
  --line:#e2e2e2;
  --white:#fff;
}
*{box-sizing:border-box;margin:0;padding:0}
html,body{width:1200px;height:2535px;overflow:hidden;background:var(--white)}
body{font-family:"Open Sans",sans-serif;color:var(--text);position:relative}
.section{position:absolute;left:0;width:1200px}
h1,h2,h3,h4{font-family:"Roboto",sans-serif;color:var(--ink)}

/* Header */
.site-header{top:0;height:101px;background:var(--white);z-index:3}
.brand{position:absolute;left:98px;top:0;width:160px;height:155px;border-radius:0 0 80px 80px;background:var(--white);display:flex;align-items:flex-end;justify-content:center;padding-bottom:38px}
.brand-name{font-family:"Roboto",sans-serif;font-weight:700;font-size:30px;color:var(--green-dark)}
.contact-bar{position:absolute;top:14px;right:100px;display:flex;gap:26px;align-items:center;font-size:15px;color:var(--ink)}
.contact-item{display:flex;align-items:center;gap:12px}
.contact-icon{width:30px;height:30px;border-radius:50%;display:flex;align-items:center;justify-content:center}
.contact-icon.mail{background:var(--blue)}
.contact-icon.phone{background:var(--green-dark)}
.main-nav{position:absolute;top:64px;right:104px;display:flex;gap:30px;font-family:"Roboto",sans-serif;font-weight:500;font-size:14px;color:var(--ink);align-items:center}

/* Hero */
.hero{top:101px;height:474px;background:linear-gradient(100deg,#a7d36a 0%,#c6e49a 35%,#8fbf4e 65%,#6e9f37 100%)}
.hero-title{position:absolute;left:130px;top:158px;font-size:52px;font-weight:700;color:var(--white);letter-spacing:.5px}
.hero-sub{position:absolute;left:132px;top:228px;font-size:24px;color:var(--white);font-family:"Roboto",sans-serif}
.hero-btn{position:absolute;left:133px;top:297px;width:167px;height:42px;border:2px solid var(--white);color:var(--white);font-family:"Roboto",sans-serif;font-size:17px;display:flex;align-items:center;justify-content:center}
.hero-arrow{position:absolute;top:200px}

/* Welcome */
.welcome{top:575px;height:417px}
.section-title{position:absolute;left:0;width:1200px;text-align:center;font-size:29px;font-weight:500}
.section-sub{position:absolute;left:0;width:1200px;text-align:center;font-size:13px;color:var(--text)}
.feature{position:absolute;top:148px;width:250px;text-align:center}
.feature-ring{width:125px;height:125px;margin:0 auto;border-radius:50%;border:3px solid var(--green);padding:5px}
.feature-disc{width:100%;height:100%;border-radius:50%;background:radial-gradient(circle at 40% 35%,#9fd04a,var(--green-dark));display:flex;align-items:center;justify-content:center}
.feature h3{font-size:20px;font-weight:400;margin-top:16px}
.feature p{font-size:12.5px;line-height:23px;margin-top:6px}

/* Supplements */
.supplements{top:992px;height:365px;background:var(--green-pale)}
.supplements h2{position:absolute;left:97px;top:54px;font-size:25px;font-weight:500}
.benefits{position:absolute;left:98px;top:108px;width:602px;list-style:none;font-size:11.5px;line-height:24px;color:var(--text)}
.benefits li{position:relative;padding-left:37px;margin-bottom:9px}
.benefits li::before{content:"";position:absolute;left:0;top:10px;width:5px;height:5px;border-radius:50%;background:var(--green)}
.benefits b{color:var(--ink);font-weight:700}
.product-shot{position:absolute;left:781px;top:51px;width:297px;height:322px;border-radius:20px;background:linear-gradient(180deg,#f4f6f8 0%,#dfe7ec 55%,#7fb84a 80%,#2d7fc4 100%)}

/* Blog */
.blog{top:1357px;height:490px}
.post{position:absolute;top:156px;width:310px}
.post-photo{width:310px;height:168px}
.post h3{font-family:"Open Sans",sans-serif;font-size:16px;font-weight:700;color:var(--ink);margin-top:20px;letter-spacing:.3px}
.post p{font-size:12.5px;line-height:25px;margin-top:6px;text-align:justify}

/* What we do */
.what{top:1847px;height:396px;background:var(--grey-bg)}
.video{position:absolute;left:101px;top:68px;width:491px;height:272px;background:linear-gradient(120deg,#b99878 0%,#e6cfb6 50%,#8a7a6c 100%)}
.play{position:absolute;left:222px;top:112px}
.what h2{position:absolute;left:660px;top:66px;font-size:29px;font-weight:500}
.what-copy{position:absolute;left:660px;top:116px;width:442px;font-size:12.5px;line-height:23px;text-align:justify}
.what-copy p+p{margin-top:14px}
.read-more{position:absolute;left:661px;top:308px;width:115px;height:37px;background:var(--blue);color:var(--white);font-size:13px;font-family:"Roboto",sans-serif;display:flex;align-items:center;justify-content:center}

/* Footer */
.site-footer{top:2243px;height:292px}
.foot-col{position:absolute;top:58px}
.foot-col h4{font-size:17px;font-weight:500;margin-bottom:16px}
.foot-col ul{list-style:none;font-size:12px;line-height:25px;color:var(--text)}
.news-lead{font-size:12px;color:var(--text);margin-bottom:14px}
.news-form{display:flex}
.news-input{width:207px;height:34px;border:1px solid var(--line);font-size:11px;color:#aaa;display:flex;align-items:center;padding-left:12px;font-style:italic;background:var(--white)}
.news-send{width:41px;height:34px;background:var(--sky);display:flex;align-items:center;justify-content:center}
.foot-rule{position:absolute;left:63px;top:240px;width:1002px;height:1px;background:var(--line)}
.copyright{position:absolute;left:0;top:264px;width:1200px;text-align:center;font-size:12px;color:var(--muted)}
</style>
</head>
<body>

<header class="section site-header">
  <div class="brand"><span class="brand-name">Verdant</span></div>
  <div class="contact-bar">
    <div class="contact-item">
      <span class="contact-icon mail"><svg width="14" height="11" viewBox="0 0 14 11"><rect x="0.8" y="0.8" width="12.4" height="9.4" fill="none" stroke="#fff" stroke-width="1.4"/><path d="M1 1l6 5 6-5" fill="none" stroke="#fff" stroke-width="1.4"/></svg></span>
      info@verdantbiome.com
    </div>
    <div class="contact-item">
      <span class="contact-icon phone"><svg width="14" height="14" viewBox="0 0 24 24"><path fill="#fff" d="M6.6 10.8a15 15 0 0 0 6.6 6.6l2.2-2.2c.3-.3.7-.4 1-.2 1.1.4 2.3.6 3.6.6.6 0 1 .4 1 1V20c0 .6-.4 1-1 1A17 17 0 0 1 3 4c0-.6.4-1 1-1h3.5c.6 0 1 .4 1 1 0 1.3.2 2.5.6 3.6.1.3 0 .7-.2 1z"/></svg></span>
      555 010 1230
    </div>
  </div>
  <nav class="main-nav">
    <span>HOME</span><span>ABOUT US</span><span>SERVICES</span><span>PRODUCTS</span><span>BLOG</span><span>TESTIMONIAL</span><span>CONTACT US</span><span>|</span>
    <svg width="13" height="13" viewBox="0 0 13 13"><circle cx="5.3" cy="5.3" r="4.2" fill="none" stroke="#1d1d1d" stroke-width="1.8"/><path d="M8.5 8.5l3.6 3.6" stroke="#1d1d1d" stroke-width="2"/></svg>
  </nav>
</header>

<section class="section hero" role="img" aria-label="Smiling family of three sitting together on bright green grass in a sunny park">
  <h1 class="hero-title">VERDANT BIOME</h1>
  <p class="hero-sub">We sell probiotic supplements.</p>
  <div class="hero-btn">GET MORE INFO</div>
  <svg class="hero-arrow" style="left:30px" width="20" height="70" viewBox="0 0 20 70"><path d="M18 2L2 35l16 33" fill="none" stroke="#fff" stroke-width="2" opacity=".8"/></svg>
  <svg class="hero-arrow" style="right:18px" width="20" height="70" viewBox="0 0 20 70"><path d="M2 2l16 33L2 68" fill="none" stroke="#fff" stroke-width="2" opacity=".8"/></svg>
</section>

<section class="section welcome">
  <h2 class="section-title" style="top:56px">WELCOME TO NUTRACUETICAL</h2>
  <p class="section-sub" style="top:100px">There are many variations of passages of Lorem Ipsum available, but the majority have suffered alteration</p>

  <div class="feature" style="left:81px">
    <div class="feature-ring"><div class="feature-disc">
      <svg width="48" height="48" viewBox="0 0 48 48"><circle cx="24" cy="16" r="10" fill="#fff"/><path d="M6 44c0-10 8-16 18-16s18 6 18 16z" fill="#fff"/></svg>
    </div></div>
    <h3>Probiotic For Women</h3>
    <p>It is a long established fact that reader will be distracted by readable</p>
  </div>
  <div class="feature" style="left:343px">
    <div class="feature-ring"><div class="feature-disc">
      <svg width="46" height="50" viewBox="0 0 46 50"><path d="M23 3l18 6v14c0 12-8 21-18 24C13 44 5 35 5 23V9z" fill="none" stroke="#fff" stroke-width="3"/><circle cx="23" cy="25" r="8" fill="none" stroke="#fff" stroke-width="2.5"/><path d="M23 20v5l3 3" stroke="#fff" stroke-width="2.5" fill="none"/></svg>
    </div></div>
    <h3>Traditional Probiotics</h3>
    <p>It is a long established fact that reader will be distracted by readable</p>
  </div>
  <div class="feature" style="left:605px">
    <div class="feature-ring"><div class="feature-disc">
      <svg width="44" height="50" viewBox="0 0 44 50"><path d="M16 4h12M18 4v16L5 44h34L26 20V4" fill="none" stroke="#fff" stroke-width="3" stroke-linejoin="round"/><path d="M11 34h22l5 9H6z" fill="#fff"/></svg>
    </div></div>
    <h3>Lab Test</h3>
    <p>It is a long established fact that reader will be distracted by readable</p>
  </div>
  <div class="feature" style="left:869px">
    <div class="feature-ring"><div class="feature-disc">
      <svg width="50" height="50" viewBox="0 0 50 50"><circle cx="22" cy="18" r="9" fill="#fff"/><path d="M11 18a11 11 0 0 1 22 0" fill="none" stroke="#fff" stroke-width="2.5"/><path d="M4 46c0-9 8-15 18-15s18 6 18 15z" fill="#fff"/><circle cx="40" cy="36" r="7" fill="#fff"/></svg>
    </div></div>
    <h3>Support</h3>
    <p>It is a long established fact that reader will be distracted by readable</p>
  </div>
</section>

<section class="section supplements">
  <h2>PROBIOTIC SUPPLEMENTS</h2>
  <ul class="benefits">
    <li><b>WHAT MAKES US DIFFERENT??</b> - Patent pending GutShield 3D 2 step acid protection. The probiotics release in the GI tract and avoid being killed in the stomach. Probiotic 40 Billion or Probiotic</li>
    <li><b>LAB TESTED</b> More effective than traditional probiotics. Developed by a Doctor who specializes in gut</li>
    <li><b>GREAT PROBIOTIC FOR MEN, PROBIOTIC FOR WOMEN, and KIDS</b> - Allergen free and made in a GMP and FDA registered facility</li>
    <li><b>IMPROVE IMMUNE SYSTEM</b> - 80% of our immune system is out gut. Take care of your gut and watch the difference in your body's health</li>
  </ul>
  <div class="product-shot" role="img" aria-label="Three white probiotic capsule bottles with green and blue labels"></div>
</section>

<section class="section blog">
  <h2 class="section-title" style="top:62px">OUR RECENT BLOG POST</h2>
  <p class="section-sub" style="top:108px">There are many variations of passages of Lorem Ipsum available, but the majority</p>

  <article class="post" style="left:100px">
    <div class="post-photo" role="img" aria-label="Smiling young woman resting her head on a man's shoulder" style="background:linear-gradient(120deg,#f1e3d3,#c79b73 60%,#efe7de)"></div>
    <h3>SED PERSPICIATIS UNDE OMNIS</h3>
    <p>Lorem ipsum dolor sit amet, consectetuer. Proin gravida nibh vel velit auctor aliquet. the far Aenean sollicitudi ravida.Lorem ipsum dolor sit amet,</p>
  </article>
  <article class="post" style="left:446px">
    <div class="post-photo" role="img" aria-label="Mother and young daughter lying together on sunny grass" style="background:linear-gradient(120deg,#9e8a3a,#d9c98f 50%,#7c8b3b)"></div>
    <h3>SED PERSPICIATIS UNDE OMNIS</h3>
    <p>Lorem ipsum dolor sit amet, consectetuer. Proin gravida nibh vel velit auctor aliquet. the far Aenean sollicitudi ravida.Lorem ipsum dolor sit amet,</p>
  </article>
  <article class="post" style="left:791px">
    <div class="post-photo" role="img" aria-label="Family in winter hats huddled together in a circle, smiling" style="background:linear-gradient(120deg,#c3642f,#e7b48a 45%,#3e5b80)"></div>
    <h3>SED PERSPICIATIS UNDE OMNIS</h3>
    <p>Lorem ipsum dolor sit amet, consectetuer. Proin gravida nibh vel velit auctor aliquet. the far Aenean sollicitudi ravida.Lorem ipsum dolor sit amet,</p>
  </article>
</section>

<section class="section what">
  <div class="video" role="img" aria-label="Video still of a laughing family with two children">
    <svg class="play" width="48" height="48" viewBox="0 0 48 48"><circle cx="24" cy="24" r="23" fill="#fff" fill-opacity=".85"/><path d="M19 14l14 10-14 10z" fill="#333"/></svg>
  </div>
  <h2>WHAT WE DO</h2>
  <div class="what-copy">
    <p>At vero eos et accusamus et iusto odio dignissimos ducimus qui blanditiis praesentium voluptatum deleniti atque corrupti quos dolores et quas molestias excepturi sint occaecati cupiditate non provident, similique sunt in culpa qui officia deserunt mollitia animi, id est laborum et dolorum fuga.</p>
    <p>At vero eos et accusamus et iusto odio dignissimos ducimus qui blanditiis praesentium voluptatum deleniti atque corrupti quos dolores et quas molestias excepturi sint occaecati cupiditate non provident, similique</p>
  </div>
  <div class="read-more">READ MORE</div>
</section>

<footer class="section site-footer">
  <div class="foot-col" style="left:63px">
    <h4>COMPANY</h4>
    <ul><li>Services</li><li>Products</li><li>Blog</li><li>Testimonial</li></ul>
  </div>
  <div class="foot-col" style="left:281px">
    <h4>NUTRACUETICAL</h4>
    <ul><li>Maplewood Academy</li><li>Finibus Bonorum</li><li>Predefined chunks</li><li>Non-characteristic</li></ul>
  </div>
  <div class="foot-col" style="left:553px">
    <h4>WHY US</h4>
    <ul><li>Ullamco laboris nisi</li><li>Fugiat nulla pariatur</li><li>Commodo consequat</li><li>Duis aute irure</li></ul>
  </div>
  <div class="foot-col" style="left:815px">
    <h4>NEWSLETTER</h4>
    <p class="news-lead">SIGN UP FOR A FREE WEEK!</p>
    <div class="news-form">
      <div class="news-input">Enter Your Mail Id</div>
      <div class="news-send"><svg width="15" height="15" viewBox="0 0 16 16"><path d="M15 1L1 7l5 2 2 6z" fill="#fff"/></svg></div>
    </div>
  </div>
  <div class="foot-rule"></div>
  <p class="copyright">Copyrights@CompanyName , All rights Reserved</p>
</footer>

</body>
</html>
```